Online shopping portal - Business Card Design

Brivanto.com.au is a complete shopping experience. Search, compare & buy items from partnered stores & receive cashbash for your purchases and referrals.
Mission
Our mission is to provide a system for entrepreneurs to create an ongoing income, while providing consumers worldwide with a better way to shop.
A product brokerage and Internet marketing company that specialises in One-to-One Marketing, Quelden Australia is a subsidiary of Quelden Norvik Worldwide, Inc.
With more than 3 million Preferred Customers and 180,000 Customer Managers worldwide, Quelden Norvik has generated over $3 billion USD in accumulated retail sales. The Company employs more than 675 people globally with international operations in Australia, United States, Canada, Taiwan, Hong Kong, Mexico & Singapore
Through revolutionary technology and the one-to-one marketing and social shopping Quelden Australia are leveraging the Internet with the power of people to create the economy of the future.
By providing online shoppers with the products and services they want and need — backed by the Company’s people power — Quelden Australia is fast becoming the World Wide Web’s ultimate online shopping destination.
As a result, we are changing the way people shop and changing the economic paradigm where anyone can become financially independent by creating their own economy — Rooted in Goods. Lifted by Folk®.
Description
Welcome to a new kind of comparison shopping site where you get PAID cashback to shop!
Simply create an account to start accumulating cash backs each time you make purchases across hundreds of trusted Partner Stores and thousands of your favorite brands through our convenient SwiftTote® for one stop shopping.
All merchant stores are backed by PELMARO.COM's 100% satisfaction guarantee.

Updates
Project Deadline Extended
Reason: Hi all,  I am extending the deadline as i'm going to be away for my birthday (and may not have time to check before the current deadline anyway)  I figure that the more time i give you the better.

Industry/Entity Type
Online Shopping
Contact Information for Business Card
Business Name: Brivanto.com.au
website: www.brivanto.com.au
Facebook: www.friendnook.com/brivanto.com.au.
Email: info@brivanto.com.au
Phone: Mirel on 0497 28 14 56
Requirements
Nice to have
- Create a Brivanto logo

```html
<!DOCTYPE html>
<html lang="en">
<head>
<meta charset="utf-8">
<title>Brivanto Business Card</title>
<link rel="stylesheet" href="https://fonts.googleapis.com/css2?family=Abel&family=Marcellus&family=Russo+One&family=Arimo:wght@400;700&display=swap">
<style>
  :root {
    --teal: #1b9cc2;
    --teal-light: #46b9da;
    --teal-dark: #0f86aa;
    --navy: #1f2464;
    --accent: #3aa9c9;
    --rule: #c9dfe8;
    --paper: #ffffff;
    --backdrop: #eeeff0;
  }
  * { margin: 0; padding: 0; box-sizing: border-box; }
  html, body { width: 1200px; height: 1000px; overflow: hidden; background: var(--backdrop); }
  .canvas { position: relative; width: 1200px; height: 1000px; }
  .card {
    position: absolute; width: 748px; height: 404px;
    background: var(--paper); overflow: hidden;
    box-shadow: 0 3px 10px rgba(0,0,0,.18);
  }
  .card-front { left: 230px; top: 37px; }
  .card-back { left: 297px; top: 511px; }
  .card-art { position: absolute; inset: 0; }
  .brand {
    position: absolute; display: flex; align-items: center; gap: 8px;
    font-family: "Russo One", sans-serif; color: var(--navy);
  }
  .brand-dot { border-radius: 50%; background: var(--teal); }
  .front-brand { left: 0; right: 0; top: 138px; justify-content: center; font-size: 40px; }
  .front-brand .brand-dot { width: 30px; height: 30px; }
  .tagline {
    position: absolute; left: 0; right: 0; text-align: center; white-space: nowrap;
    font-family: "Marcellus", serif; color: var(--accent); text-transform: uppercase;
  }
  .tagline-top { top: 217px; font-size: 14px; letter-spacing: 2.4px; }
  .tagline-main { top: 239px; font-size: 19px; letter-spacing: 2.6px; }
  .tagline-sub { top: 264px; font-size: 14px; letter-spacing: 2.2px; }
  .rule { position: absolute; left: 267px; width: 228px; height: 1px; background: var(--rule); }
  .back-brand { left: 115px; top: 26px; font-size: 28px; }
  .back-brand .brand-dot { width: 22px; height: 22px; }
  .social-curve {
    position: absolute; left: 428px; top: 58px; transform: rotate(7deg);
    font-family: "Arimo", sans-serif; font-weight: 700; font-size: 11px; color: var(--navy);
    white-space: nowrap;
  }
  .welcome, .reach {
    position: absolute; left: 0; right: 0; text-align: center;
    font-family: "Abel", sans-serif; color: var(--navy); font-weight: bold;
  }
  .welcome { top: 124px; font-size: 21px; line-height: 30px; }
  .reach { top: 300px; font-size: 18px; line-height: 24px; }
  .contact {
    position: absolute; display: flex; align-items: center; gap: 22px; white-space: nowrap;
    font-family: "Arimo", sans-serif; font-size: 15px; color: var(--navy);
  }
  .contact svg { width: 28px; height: 22px; flex: none; }
</style>
</head>
<body>
<div class="canvas">

  <section class="card card-front">
    <svg class="card-art" viewBox="0 0 748 404" aria-hidden="true">
      <defs>
        <linearGradient id="bandFront" x1="0" y1="0" x2="0" y2="1">
          <stop offset="0" stop-color="#0f86aa"/>
          <stop offset="1" stop-color="#46b9da"/>
        </linearGradient>
      </defs>
      <path d="M0 0H748V96C660 60 560 28 430 30C300 32 200 80 110 80C60 80 25 60 0 52Z" fill="url(#bandFront)"/>
      <path d="M0 56C25 64 60 84 110 84C200 84 300 36 430 34C560 32 660 64 748 100" fill="none" stroke="#fff" stroke-width="2"/>
      <path d="M0 60C25 68 60 88 110 88C200 88 300 40 430 38C560 36 660 68 748 104" fill="none" stroke="#1b9cc2" stroke-width="1"/>
      <rect x="0" y="341" width="748" height="63" fill="#1b9cc2"/>
    </svg>
    <div class="brand front-brand"><span class="brand-dot"></span>Brivanto</div>
    <div class="rule" style="top:210px"></div>
    <p class="tagline tagline-top">Better Way to Shop</p>
    <p class="tagline tagline-main">3 Million Preferred Customers</p>
    <p class="tagline tagline-sub">180,000 Customer Managers</p>
    <div class="rule" style="top:289px"></div>
  </section>

  <section class="card card-back">
    <svg class="card-art" viewBox="0 0 748 404" aria-hidden="true">
      <defs>
        <linearGradient id="bandBack" x1="0" y1="0" x2="0" y2="1">
          <stop offset="0" stop-color="#0f86aa"/>
          <stop offset="1" stop-color="#46b9da"/>
        </linearGradient>
      </defs>
      <path d="M0 0H748V88C650 66 520 70 380 82C220 96 80 90 0 38Z" fill="url(#bandBack)"/>
      <path d="M0 42C80 94 220 100 380 86C520 74 650 70 748 92" fill="none" stroke="#fff" stroke-width="2"/>
      <path d="M0 46C80 98 220 104 380 90C520 78 650 74 748 96" fill="none" stroke="#1b9cc2" stroke-width="1"/>
      <rect x="0" y="360" width="748" height="44" fill="#1b9cc2"/>
    </svg>
    <div class="brand back-brand"><span class="brand-dot"></span>Brivanto</div>
    <p class="social-curve">www.friendnook.com/brivanto.com.au.</p>

    <p class="welcome">Welcome to a new kind of comparison shopping site where you get PAID<br>cashback to shop!</p>

    <div class="contact" style="left:72px;top:197px">
      <svg viewBox="0 0 28 22"><circle cx="14" cy="11" r="10" fill="#1b9cc2"/></svg>
      www.brivanto.com.au
    </div>
    <div class="contact" style="left:72px;top:237px">
      <svg viewBox="0 0 28 22"><rect x="5" y="5" width="18" height="12" fill="#1f2464"/><path d="M5 5L14 12L23 5" fill="none" stroke="#fff" stroke-width="1.5"/></svg>
      info@brivanto.com.au
    </div>
    <div class="contact" style="left:370px;top:199px">
      <svg viewBox="0 0 28 22"><path d="M4 8C4 4 24 4 24 8V10H18V8H10V10H4Z" fill="#1f2464"/><rect x="7" y="11" width="14" height="8" rx="1" fill="#1f2464"/><circle cx="14" cy="15" r="2" fill="#fff"/></svg>
      0497 28 14 56
    </div>
    <div class="contact" style="left:370px;top:237px">
      <svg viewBox="0 0 28 22"><circle cx="14" cy="11" r="10" fill="#1f2464"/></svg>
      www.friendnook.com/brivanto.com.au.
    </div>

    <p class="reach">The Company employs more than 675 people globally with international&nbsp; operations<br>in Australia , United States , Canada , Hong Kong&nbsp; Mexico &amp; Singapore.</p>
  </section>

</div>
</body>
</html>
```